A book about police officer shootings needs a dynamic cover design

I've almost completed a book on officer involved shootings...a very hot topic today. The title is "R.K.V. Beyond The Silence Broke." (emphasis on "Beyond The Silence") It details three separate shooting incidents, all within the same law enforcement family.I need a professional looking book cover that helps capture the drama. I attached a file of something I put together that is close, but I am concerned about "readability" and want a more professional look. I included a photo that I took off the internet of a gun being shot. That particular photo can stay or go, or be altered, but I like the perspective of the photo being fired from the person behind it. I wanted the cover to have the characteristics and color of a police uniform, utilizing blues, silvers, and maybe a little gold. I'm concerned about making sure the font and colors are also easy to read. I also will be working on a website design for "Beyond The Silence.Com" once the book hits the market. The back cover will incorporate the same colors, but only be a picture and excerpts from the book. I've included both for your review.

Target Market(s)

Law Enforcement, Christian, Media

Font styles to use
Sans Serif

Requirements
Must have
• A professional and readable appearance, that captures the drama of the topic. All the wording on the sample cover I attached, unless you come up with something better. A gun being fired from the perspective of the officer pulling the trigger. The size of the book will be the standard 6 x 9 in size. "Beyond The Silence" will eventually be my website domain and social media promotion hashtag.
Nice to have
• I would like the cover to incorporate the colors of a police uniform and badge, traditionally, navy blue, silver and some gold.
Should not have
• No police badge with a black band across. Not my topic.

```html
<!DOCTYPE html>
<html lang="en">
<head>
<meta charset="utf-8">
<title>R.K.V. Beyond The Silence Broke — Book Cover</title>
<link href="https://fonts.googleapis.com/css2?family=Oswald:wght@200;300&family=Michroma&family=Montserrat:wght@500;600&display=swap" rel="stylesheet">
<style>
  :root {
    --navy-deep: #050b16;
    --navy: #0d2136;
    --steel-blue: #2e5c82;
    --haze-blue: #5a8bb3;
    --silver-light: #f4f6f8;
    --silver-mid: #b8c2cc;
    --silver-dark: #5f6a75;
    --gold-flash: #ffd46a;
    --gold-core: #fff3c2;
    --text-white: #ffffff;
    --author-grey: #a9adb1;
  }
  * { margin: 0; padding: 0; box-sizing: border-box; }
  html, body { width: 1200px; height: 830px; overflow: hidden; background: var(--navy-deep); }

  .cover-spread {
    position: relative;
    width: 1200px;
    height: 830px;
    overflow: hidden;
    background:
      radial-gradient(ellipse 420px 300px at 300px 300px, rgba(90,139,179,.35), transparent 70%),
      radial-gradient(ellipse 500px 420px at 900px 560px, rgba(46,92,130,.55), transparent 70%),
      linear-gradient(180deg, var(--navy) 0%, #0a1828 55%, var(--navy-deep) 100%);
  }

  /* Front cover photo area: officer firing handgun */
  .front-photo {
    position: absolute;
    left: 560px; top: 0;
    width: 640px; height: 520px;
    background:
      radial-gradient(circle at 255px 70px, var(--gold-core) 0, var(--gold-flash) 40px, rgba(230,150,40,.55) 110px, rgba(40,80,120,0) 230px),
      radial-gradient(ellipse 260px 420px at 470px 200px, rgba(20,32,48,.85), transparent 75%),
      linear-gradient(160deg, rgba(30,60,90,.5), rgba(10,20,35,0));
  }

  /* Back cover panel */
  .back-panel {
    position: absolute;
    left: 68px; top: 52px;
    width: 456px; height: 722px;
    border-radius: 8px;
    border: 5px solid var(--silver-mid);
    box-shadow: inset 0 0 0 2px var(--silver-dark), 0 0 0 1px var(--silver-light), 0 0 16px rgba(0,0,0,.7);
    background:
      radial-gradient(ellipse 300px 260px at 60% 20%, rgba(90,139,179,.35), transparent 70%),
      linear-gradient(180deg, rgba(13,33,54,.75), rgba(8,20,36,.85));
    color: var(--text-white);
    font-family: 'Montserrat', sans-serif;
    text-align: center;
  }
  .back-quote {
    position: absolute; top: 38px; left: 0; right: 0;
    font-size: 14.5px; font-weight: 600; line-height: 18px; letter-spacing: .3px;
  }
  .family-photo {
    position: absolute; left: 117px; top: 73px;
    width: 200px; height: 232px;
    background: linear-gradient(180deg, #b7c7d6 0%, #6d7a84 45%, #3e4b55 100%);
    border: 1px solid rgba(255,255,255,.5);
  }
  .photo-captions {
    position: absolute; top: 316px; left: 0; right: 0;
    display: flex; justify-content: center; gap: 14px;
    font-size: 9.5px; font-weight: 600; letter-spacing: .3px;
  }
  .story { position: absolute; left: 22px; right: 22px; }
  .story-title {
    font-size: 11px; font-weight: 600; font-variant: small-caps;
    text-decoration: underline; margin-bottom: 4px; letter-spacing: .4px;
  }
  .story-excerpt {
    font-size: 10.4px; font-weight: 500; font-variant: small-caps;
    line-height: 14.2px; letter-spacing: .25px;
  }
  .story--dale  { top: 344px; }
  .story--mason { top: 448px; }
  .story--grant { top: 568px; }
  .story--grant .story-excerpt { line-height: 16.8px; }

  /* Spine */
  .spine-title {
    position: absolute;
    left: 578px; top: 72px;
    width: 696px; height: 36px;
    transform-origin: 0 0;
    transform: translate(36px, 0) rotate(90deg);
    font-family: 'Michroma', sans-serif;
    font-size: 25px; line-height: 36px;
    color: var(--text-white);
    white-space: nowrap;
    letter-spacing: 1px;
  }
  .spine-title .initials { font-family: 'Oswald', sans-serif; font-weight: 300; font-size: 30px; }

  /* Front title */
  .title {
    position: absolute; left: 640px; width: 560px;
    text-align: center;
    background: linear-gradient(180deg, var(--silver-light) 0%, var(--silver-mid) 45%, var(--silver-dark) 60%, var(--silver-light) 100%);
    -webkit-background-clip: text; background-clip: text;
    color: transparent;
    filter: drop-shadow(2px 3px 3px rgba(0,0,0,.75));
    white-space: nowrap;
  }
  .title-initials { top: 96px; font-family: 'Oswald', sans-serif; font-weight: 200; font-size: 164px; line-height: 170px; left: 670px; width: 440px; letter-spacing: 2px; }
  .title-beyond  { top: 268px; font-family: 'Michroma', sans-serif; font-size: 80px; line-height: 100px; left: 644px; width: 550px; }
  .title-the     { top: 380px; font-family: 'Michroma', sans-serif; font-size: 82px; line-height: 100px; left: 740px; width: 360px; }
  .title-silence { top: 500px; font-family: 'Michroma', sans-serif; font-size: 60px; line-height: 80px; left: 662px; width: 510px; }
  .title-broke   { top: 582px; font-family: 'Michroma', sans-serif; font-size: 68px; line-height: 90px; left: 716px; width: 430px; }

  .badge {
    position: absolute; left: 656px; top: 664px;
    width: 144px; height: 144px;
  }
  .author-name {
    position: absolute; left: 812px; top: 728px;
    font-family: 'Michroma', sans-serif; font-size: 37px; line-height: 50px;
    color: var(--author-grey);
    white-space: nowrap;
  }
</style>
</head>
<body>
<main class="cover-spread">

  <div class="front-photo" role="img" aria-label="Photo from the officer's perspective of a hand firing a handgun, with a bright golden muzzle flash against a dark blue uniform"></div>

  <section class="back-panel">
    <p class="back-quote">“YOU CANNOT RELY ON ANYONE BUT<br>YOURSELF TO SAVE YOUR LIFE…”</p>

    <div class="family-photo" role="img" aria-label="Photo of three family members standing together, one in a suit, one in a polo shirt, one in police uniform"></div>

    <p class="photo-captions">
      <span>LT. DALE CORWIN</span><span>MASON CORWIN</span><span>GRANT CORWIN</span>
    </p>

    <article class="story story--dale">
      <h2 class="story-title">Dale’s Story</h2>
      <p class="story-excerpt">“And then I heard it. The unmistakable sound of a shotgun being racked. And then another one. I was hit with near-binding light from police flashlights, but was still able to make out the silhouettes of officers taking cover behind their patrol car doors… All weapons pointed directly at me…”</p>
    </article>

    <article class="story story--mason">
      <h2 class="story-title">Mason’s Story</h2>
      <p class="story-excerpt">“Mason stood over him, holding the shotgun in his left hand and his now empty handgun in his right. He stood there in stunned disbelief at how a routine call had escalated into a violent confrontation in a matter of seconds. The stench emanating from the house, mixed with the smell of gunpowder and blood, was almost overwhelming.”</p>
    </article>

    <article class="story story--grant">
      <h2 class="story-title">Grant’s Story</h2>
      <p class="story-excerpt">“Grant desperately wanted to stay with Tom, but the danger still presented by Hollis was paramount. As Grant rushed towards the suspended vehicle, the door suddenly opened. Hollis climbed out and dropped to the ground. He stood and faced Grant like a raging bull. If the bull charged, Grant was prepared to shoot again…”</p>
    </article>
  </section>

  <h2 class="spine-title"><span class="initials">R.K.V.</span> Beyond The Silence Broke</h2>

  <h1>
    <span class="title title-initials">R.K.V.</span>
    <span class="title title-beyond">BEYOND</span>
    <span class="title title-the">THE</span>
    <span class="title title-silence">SILENCE</span>
    <span class="title title-broke">BROKE</span>
  </h1>

  <svg class="badge" viewBox="0 0 144 144" role="img" aria-label="Silver police badge illustration">
    <defs>
      <radialGradient id="badge-fill" cx="40%" cy="35%" r="70%">
        <stop offset="0" stop-color="#eef1f4"/>
        <stop offset=".6" stop-color="#9aa4ae"/>
        <stop offset="1" stop-color="#4c5660"/>
      </radialGradient>
    </defs>
    <circle cx="72" cy="72" r="66" fill="url(#badge-fill)"/>
  </svg>

  <p class="author-name">AUHOR NAME</p>
</main>
</body>
</html>
```